webpage design for www.brightpathYOU.com

Hi-
I am creating a website about weight loss through healthy eating. The target audience is 80% women, of all races and ethnic backgrounds, in the 35-55 age range, all of whom are overweight and want to lose weight.
At first (which is where you come in), the website will be strictly informational, and products for sale will be added later.
Obviously not all of the following information can be incorporated into the design, but to give you some background, here is what I am doing.
First thing the site visitor needs to know is what the website is about. It’s about them, and how they can lose weight effectively. It’s only secondarily about me, and the w
ebsite must talk about me only from the point of view of how can I help them. It is your job to create a webpage where I can do just that. I have the content of this page ready to go, but I need you to create a beautiful, enticing, and effective framework to put it all in. You do not need to enter any copy except for the small amount noted below.
My clients are looking for a weight loss method or program that is effective, healthy, and long-lasting. This system addresses those needs. It's important for the clients to know that with the brightpathYOU system, there is no hunger, no deprivation, no pills, no weighing foods or calorie counting, no special products to buy, among other things.
And not only does the weight come off, but there are other health benefits as well. The brightpathYOU system can lower cholesterol, blood pressure, dependence on insulin for type 2 diabetics, reduce risk of heart disease and certain types of cancer, among other things-and this has been medically documented.
When I say "healthy eating", the focus of this program is on vegetables, fruits, and grains, with no added fat, but I do not want the main page to highlight that, since the whole notion of lots of veggies can scare people away. Pictures of fruits and veggies are fine. I'll introduce scary words like “vegan” and “no added fat” into the written materials and in the video, but there is no point in chasing people away too quickly!
The banner headline should have incorporated into it, in addition to the business name, the following: "Lose weight...improve your looks...improve your health...transform your life". You will need to choose a typeface and add this copy.
I would like to have a collage of healthy, happy, slender people of all ages (mostly women), in group and social settings-but not all exercising or doing yoga or jogging, since many of my target audience are couch potatoes (at least right now). If you do use any pictures of overweight people, they should be solitary, not part of a group, and definitely not looking happy!. I was thinking of having this only in the banner at top, but if you find a way to make the site attractive by adding a thin border with this as well, feel free.
Or, since I am not a design person by any stretch of the imagination, if you have another idea as to the banner design and the rest, I am certainly open to it.
In addition to the banner headline, I want a two-column design on the lower section, one being a narrower sidebar on the right, with a place for the customer to enter his/her name, and the following: Free video & eBook" "Every Plate Tells A Story, Every Meal Builds A Habit-And How You Can Shape Yours Today", and they get this in exchange for entering their first and last name, and email address. I can link this to AWeber later. I have a video widget, as well as a bunch more, in place, so you do not need to create or order those.
I will later add something to this section about no spam will be sent.
Below that in the same thinner column on the right should be an archives section, which you will need to create if the Wordpress theme doesn't have it already. This should be the same on all pages, except the single column pages, and since they will have sales pitches, should not have anything else.
The wider, main column I want to have three particular areas: One, is video. Two is text. Three is comments.
I will be using a LOT of video, but below each video I want to be able to place the text for the video (not everyone wants to watch a video), I want a static first page, but no comments section on the first page (I may want to add a comments section later, but not now).
The next page will be a basic "about me" page. This will be a video with text below in the main section, and will have the same enter your email info on the right side bar. No need to have "comments" below this. I've uploaded a picture of me, which should appear on this page, as well as on the main page.
Then will be a blog page, again the same layout: videos, which I can add to consecutively, with "comments" below, (which I can approve or disapprove before they get posted), with the offer in the right sidebar. Any videos will also show up in the archives section.
And a "recipes" page, video and text, plus comments section, with the email offer in the sidebar. These will show up as an archives section as well. I’ll add recipes and cooking videos later.
Then will be a "Products" page, which will for now be blank (I haven't created them yet), but with the email offer in the right side bar. No comments section to this one.
And a Contact Us page, no comments section either. I'll add the contact information later.
Across bottom of each page, perhaps in a somewhat contrasting color, will be a disclaimer, which I’ll need to be able to edit. This will be in small print, and should say something like, “This website expresses the opinions of the author, is intended for informational and educational purposes only, should not be construed as medical or dietary advice, and is not intended to be a substitute for same. Before changing diets, medications, or before undertaking a weight loss regimen, be sure to consult with your physician. This information is not intended to diagnose or treat any illness or health problems you may be experiencing, so kindly address your doctor with these concerns.” You can copy and paste this text.
Each page should also say “copyright 2014, Ned Brook”, which you will need to add.
Beyond that I will need single blank column pages which I will later make into landing, thank you, and so on pages. This will not be visible from the main page, though.

This will be done in Wordpress. I have the URL and the page is set up on Wordpress already, but I will need you to integrate the design into my Wordpress site when it is completed, so you will need a working knowledge of Wordpress. So the final winner will need to have the capability of coding the design and uploading it into my website and server. When you are done, it will be a complete and turnkey website, and all I have to do is add the copy and videos.

I am not particular as to a Wordpress theme, as long as it's an unpaid one, but if you find a paid one that you think is useable and needs to be paid for, let me know so I can check it out.
And I will need to be easily able to change and edit anything in the webpage on Wordpress at the end, after you are finished, with NO HTML, so any theme must be dummy friendly (I am the dummy, by the way!). (I have a basic familiarity with Wordpress, but none of HTML.)

Hopefully this gives you more than enough information to work with. Even though this page is a bit complicated, the actual website should be pretty simple looking, not busy or full of distractions, with only a few focal points.
Updates

Hi-information has been updated, I've changed my status to "committed", and I've uploaded a lot of pictures of fruit and veggies for you to use.  Thanks for your attention!
Ned

Target Market(s)

As stated above, "The target audience is 80% women, of all races and ethnic backgrounds, in the 35-55 age range, all of whom are overweight and want to lose weight."

Industry/Entity Type

Cooking

Font styles to use
Serif

Requirements
Must have
• The home page serves two purposes: one, to introduce the reader to the material, but two, and equally important, to build my email list. To that end, the opt in form on the right should say prominently, Free video & eBook" "Every Plate Tells A Story, Every Meal Builds A Habit-And How You Can Shape Yours Today", and below that should be the opt in boxes.
The banner can be scrolling, to attract ATTENTION, should lead to the ACTION of watching the video, which will have in it a CALL TO ACTION of signing up for the hopefully compelling OFFER of the free ebook and video-and of course the newsletter. My purpose on page one is to directly address the question of "What's in it for me?", and then to deliver with the video and ebook offer.
I've uploaded a bunch of pictures of veggies and fruit-feel free to use them, as they are all mine.
Possibly a scrolling banner could be used with alternating pictures of happy, slender people alternating with pictures, and the captions of "lLose weight...improve your looks...improve your health...transform your life"

Emphasis should be on healthy eating, not on pounds lost or measuring one's waist or some such thing.

Banner headline should include: ""Lose weight...improve your looks...improve your health...transform your life"
Should not have
• Please avoid pictures of picture-perfect people, scales, and so on-I do not want this to be some generic, cookie-cutter weight loss web site. This is about weight loss from a different point of view-and I don't think this will come across in the webpage, but the concept will be introduced later. It's about weight loss as a byproduct of changing eating habits from unhealthy to healthy.

```html
<!DOCTYPE html>
<html lang="en">
<head>
<meta charset="utf-8">
<title>brightpathYOU – Healthy Eating</title>
<link rel="stylesheet" href="https://fonts.googleapis.com/css2?family=Quicksand:wght@300;400;500&family=Arimo:wght@400&display=swap">
<style>
  :root {
    --cream: #f0e6df;
    --brown: #8b5e34;
    --brown-light: #a0703e;
    --berry: #940a3f;
    --berry-dark: #8b0038;
    --field: #d9a9b6;
    --hero-red: #a30d12;
    --hero-dark: #4a0608;
    --ink: #222222;
    --grey-frame: #dde0e3;
    --player: #1c1c1c;
    --dot: #4a4a4a;
    --sky: #1b9bd6;
    --navy: #3b5998;
    --scarlet: #c4302b;
  }
  * { box-sizing: border-box; margin: 0; padding: 0; }
  html, body { width: 1029px; height: 1200px; overflow: hidden; background: #fff; }
  body { position: relative; font-family: "Quicksand", sans-serif; }

  .site-header { position: absolute; left: 0; top: 0; width: 1029px; height: 72px; background: var(--cream); }
  .brand { position: absolute; display: flex; align-items: center; gap: 8px; color: var(--brown); font-family: "Quicksand", sans-serif; font-weight: 500; }
  .brand-mark { background: var(--brown); border-radius: 3px; }
  .site-header .brand { left: 21px; top: 17px; font-size: 29px; }
  .site-header .brand-mark { width: 35px; height: 35px; }
  .main-nav { position: absolute; right: 22px; top: 23px; font-size: 18px; color: var(--brown); }
  .main-nav a { color: var(--brown); text-decoration: none; }
  .main-nav .sep { margin: 0 9px; }

  .hero { position: absolute; left: 0; top: 72px; width: 1029px; height: 318px;
    background: radial-gradient(ellipse at 55% 60%, var(--hero-red) 0%, #7d0a0e 55%, var(--hero-dark) 100%);
    border-top: 3px solid #1a0203; }
  .hero-photo { position: absolute; left: 0; top: 0; width: 560px; height: 315px;
    background: linear-gradient(100deg, #c9b3a5 0%, #8aa7bf 45%, #d6c2a4 70%, rgba(163,13,18,0) 100%); }
  .hero-copy { position: absolute; left: 544px; top: 86px; width: 470px; color: #fff; font-weight: 300; }
  .hero-copy .title { font-size: 48px; line-height: 1.05; }
  .hero-copy .sub { font-size: 21px; line-height: 1.4; }
  .hero-copy .line { font-size: 36px; line-height: 1.15; margin-top: 2px; }

  .produce { position: absolute; left: 0; top: 380px; width: 580px; height: 104px;
    background: radial-gradient(ellipse 110px 50px at 110px 40px, #d9a23a 0%, #8e9b3a 60%, rgba(255,255,255,0) 100%),
                radial-gradient(ellipse 135px 45px at 445px 38px, #c2412a 0%, #6e9a3c 60%, rgba(255,255,255,0) 100%); }
  .slider-dots { position: absolute; left: 913px; top: 413px; display: flex; gap: 4px; }
  .slider-dots span { width: 13px; height: 13px; background: var(--dot); }
  .slider-dots .active { background: var(--hero-red); }

  .video-card { position: absolute; left: 29px; top: 512px; width: 445px; height: 328px; background: var(--grey-frame); border-radius: 9px; }
  .player { position: absolute; left: 12px; top: 9px; width: 421px; height: 308px; background: var(--player); border-radius: 6px; }
  .player-screen { position: absolute; left: 7px; top: 13px; width: 407px; height: 245px;
    background: linear-gradient(120deg, #cfd8d4 0%, #e7d4b8 45%, #f2efe9 70%, #9fc0a0 100%); }
  .player-controls { position: absolute; left: 7px; top: 264px; width: 407px; height: 36px; }
  .play-badge { position: absolute; left: 162px; top: 84px; }

  .intro-text { position: absolute; left: 30px; top: 862px; width: 458px; font-family: "Arimo", sans-serif; font-size: 14.5px; line-height: 18px; color: var(--ink); }
  .learn-more { position: absolute; left: 30px; top: 933px; font-family: "Arimo", sans-serif; font-size: 15px; color: var(--berry-dark); text-decoration: none; }

  .optin { position: absolute; left: 549px; top: 512px; width: 450px; height: 441px; background: var(--berry); border-radius: 8px; color: #fff; }
  .optin h2 { position: absolute; left: 28px; top: 38px; font-weight: 300; font-size: 39px; line-height: 1; }
  .optin p { position: absolute; left: 29px; top: 90px; width: 400px; font-weight: 400; font-size: 18px; line-height: 25px; }
  .field { position: absolute; left: 25px; width: 386px; height: 40px; background: var(--field); border-radius: 6px;
    color: var(--berry-dark); font-size: 19px; padding: 8px 19px; }
  .field.first { top: 174px; } .field.last { top: 225px; } .field.email { top: 277px; }
  .cta { position: absolute; left: 26px; top: 338px; width: 222px; height: 52px; background: var(--cream); border-radius: 7px;
    color: var(--berry-dark); font-size: 20px; text-align: center; line-height: 52px; }

  .site-footer { position: absolute; left: 0; top: 1010px; width: 1029px; height: 119px; background: var(--cream); }
  .site-footer .brand { left: 16px; top: 28px; font-size: 22px; }
  .site-footer .brand-mark { width: 27px; height: 27px; }
  .copyright { position: absolute; left: 16px; top: 68px; font-family: "Arimo", sans-serif; font-size: 11px; color: var(--brown-light); }
  .footer-nav { position: absolute; left: 349px; top: 27px; font-family: "Arimo", sans-serif; font-size: 14.5px; }
  .footer-nav a { color: var(--brown); text-decoration: none; margin-right: 9px; }
  .social { position: absolute; left: 871px; top: 23px; display: flex; gap: 15px; }
  .social span { width: 25px; height: 25px; }
  .social .s1 { background: var(--sky); } .social .s2 { background: var(--navy); } .social .s3 { background: var(--scarlet); }
  .like-badges { position: absolute; left: 875px; top: 60px; display: flex; gap: 6px; }
  .like-badges span { height: 18px; border: 1px solid #c9c9c9; background: #f7f7f7; border-radius: 2px; }

  .disclaimer { position: absolute; left: 0; top: 1140px; width: 1029px; text-align: center; font-family: "Arimo", sans-serif; font-size: 10px; line-height: 12.5px; color: #333; }
</style>
</head>
<body>
  <header class="site-header">
    <div class="brand"><span class="brand-mark"></span>brightpathYOU</div>
    <nav class="main-nav">
      <a href="#">home</a><span class="sep">|</span><a href="#">about us</a><span class="sep">|</span><a href="#">what we do</a><span class="sep">|</span><a href="#">contact us</a>
    </nav>
  </header>

  <section class="hero">
    <div class="hero-photo" role="img" aria-label="Smiling couple sharing a fresh salad and a fruit drink"></div>
    <div class="hero-copy">
      <div class="title">Lose weight...</div>
      <div class="sub">improve your looks...improve your health...</div>
      <div class="line">transform your life</div>
    </div>
  </section>
  <div class="produce" role="img" aria-label="Pile of fresh fruit beside a basket of vegetables"></div>
  <div class="slider-dots"><span></span><span></span><span></span><span class="active"></span><span></span></div>

  <div class="video-card">
    <div class="player">
      <div class="player-screen" role="img" aria-label="Video still of a woman in a kitchen beside a fridge full of fresh produce"></div>
      <svg class="play-badge" width="88" height="88" viewBox="0 0 88 88" aria-hidden="true">
        <circle cx="44" cy="44" r="40" fill="none" stroke="#fff" stroke-width="5"/>
        <path d="M34 26 L64 44 L34 62 Z" fill="#fff"/>
      </svg>
      <svg class="player-controls" viewBox="0 0 407 36" aria-hidden="true">
        <rect x="0" y="0" width="407" height="4" fill="#555"/>
        <circle cx="8" cy="2" r="6" fill="#ddd"/>
        <rect x="20" y="16" width="4" height="12" fill="#aaa"/><rect x="27" y="16" width="4" height="12" fill="#aaa"/>
        <path d="M55 19 h5 l6 -5 v16 l-6 -5 h-5 z" fill="#aaa"/>
        <text x="86" y="26" font-family="Arimo, sans-serif" font-size="10" fill="#fff">00:00 <tspan fill="#aaa">/ 18:50</tspan></text>
        <circle cx="277" cy="22" r="5" fill="none" stroke="#aaa" stroke-width="2.5"/>
        <circle cx="303" cy="22" r="5" fill="#aaa"/>
        <rect x="323" y="17" width="14" height="9" fill="none" stroke="#fff" stroke-width="2"/>
        <rect x="349" y="16" width="16" height="11" fill="none" stroke="#aaa" stroke-width="1.5"/>
        <path d="M377 16 h4 M377 16 v4 M393 16 h-4 M393 16 v4 M377 28 h4 M377 28 v-4 M393 28 h-4 M393 28 v-4" stroke="#aaa" stroke-width="1.5"/>
      </svg>
    </div>
  </div>

  <p class="intro-text">Ut wisi enim ad minim veniam, quis nostrud exerci tation ullamcorper suscipit lobortis nisl ut aliquip ex ea commodo consequat. Duis autem vel eum iriure dolor in hendrerit in vulputate velit esse molestie.</p>
  <a class="learn-more" href="#">Learn more »</a>

  <aside class="optin">
    <h2>Free Video &amp; eBook</h2>
    <p>Every Plate Tells A Story, Every Meal Builds A Habit-And How You Can Shape Yours Today</p>
    <div class="field first">first name</div>
    <div class="field last">last name</div>
    <div class="field email">email address</div>
    <div class="cta">Get Free eBook Now</div>
  </aside>

  <footer class="site-footer">
    <div class="brand"><span class="brand-mark"></span>brightpathYOU</div>
    <div class="copyright">© 2014 brightpathYOU. All Rights Reserved</div>
    <nav class="footer-nav"><a href="#">Home</a><a href="#">About Us</a><a href="#">What We Do</a><a href="#">Contact Us</a><a href="#">Terms</a><a href="#">Privacy</a></nav>
    <div class="social"><span class="s1"></span><span class="s2"></span><span class="s3"></span></div>
    <div class="like-badges"><span style="width:44px"></span><span style="width:29px"></span></div>
  </footer>

  <div class="disclaimer">
    Disclaimer: Lorem ipsum dolor sit amet, consectetur adipisicing elit, sed do eiusmod tempor incididunt ut labore<br>
    et dolore magna aliqua. Ut enim ad minim veniam, quis nostrud exercitation ullamco laboris nisi ut aliquip ex ea commodo consequat. Duis aute irure dolor in reprehenderit in<br>
    voluptate velit esse cillum dolore eu fugiat nulla pariatur. Excepteur sint occaecat cupidatat non proident, sunt in culpa qui officia deserunt mollit anim id est laborum.
  </div>
</body>
</html>
```